Book Marketing Site for authors needs redesign

I need a site redesign for the site www.quornvale.com I would like to have it designed/created in Wordpress so that I can change/edit the text as necessary. Ideally, we can simplify the site so that Wordpress updates do not impact the functionality of the site.

I want to continue to use the Quornvale logo, so I would like the site to work the existing logo. I am also planning to add the tag line Reader Outreach Made Plain so please incorporate the tag line with the logo and the site.

Initially, I would like to see the page design template and then once that is approved, you to program the site. Wherever, I have indicated that we would capture email addresses; I would like to set it up so that the names are captured in my Mailwick Hub account.

Below are the elements that will need to be part of the site:
_______

Elements that should be above the fold:

• Chirpnet, Friendwall, Orbix+ and Workloop buttons with the copy “Connect with Dorothy”
o
• The copy “Sign up for our free newsletter and receive our list of Top Chirpnet Tips for Authors Free!” with a box to enter email address. The button should say “Go” not "Submit".
• A space/box for a short, 10-15 word testimonials. The testimonials will need to change from page to page.

Nav Bar/sub nav bars

Services
Packages Speaking Testimonials
FAQ
-
About Us
Speaking
-
Resources
-
Our clients
Testimonials
-
Blog
-
Contact Us

Home page
• Should have the following copy:
High Impact Book Marketing for Authors

Quornvale Marketing is book marketing service that that provides authors with an effective,
affordable approach to marketing their book.

We provide marketing coaching and consulting services that accelerate book sales, target your ideal reader and develop a community of fans that will promote your book for you.

Using high impact, low cost marketing strategies, we will develop a book marketing strategy that achieves your goals and accommodates your budget

Do you
• Want to be a best selling author, but need someone to show you the way

• Wonder what is the secret to achieving high book sales?

• Worry that you aren’t doing the right things to ensure that your book is a success?

• Need someone to help keep your spirits up and maintain momentum?

• Please put the following copy in a box at the bottom of the copy.
o Are you ready for results? Call now for a free consultation 214-555-0183

Services Page
• Copy to come

Packages Page

FAQ Page
• Same as existing site

About page
• Same as existing site

Speaking Page

Speaking

If you’re looking to create an exceptional program that your attendees won’t be able to stop talking about, you have found it!

Dorothy Pellam, a leader in book marketing, has ability to make sophisticated internet concepts easy and accessible, and the unique ability to not only to inform, but also to inspire. Her presentations leave participants with tangible, actionable ideas proven to increase book sales.

Dorothy's talks combine practical step-by-step instructions, real-life examples with plenty of humor. Call 214-555-0183 to book her now!

Dorothy’s most popular talks:

• Unlocking the Power of Pagehive
• How to Simplify Social Media
• The Ideal Author Website
• Bazario: What You Need to Know to Succeed

Resources page
• Same as existing site

Clients
• Same as existing site

Testimonials
• I would like to be able to put a image of book cover next to the testimonial on this page.

Blog page
• Please add the following elements:
• A way to sign up for the blog via RSS
o Each blog article should have a way to Friendwall like, Tweet, O+, Pokk and Trundlefind the article

Contact us page
• Same as existing site

Site Map
• Please make sure to include a site map.

Chirpnet and Friendwall headers
• Please provide both with consistent branding.

Target Market(s)

Clients are both traditionally and indie published authors trying to be the next M.K. Orwin!

Industry/Entity Type

Marketing

Requirements
Must have
• Elements that should be above the fold:

o

```html
<!DOCTYPE html>
<html lang="en">
<head>
<meta charset="utf-8">
<title>Quornvale — High Impact Book Marketing for Authors</title>
<link href="https://fonts.googleapis.com/css2?family=Krona+One&family=Michroma&family=Oswald:wght@500&family=PT+Sans:wght@400;700&display=swap" rel="stylesheet">
<style>
  :root {
    --navy: #0a4a94;
    --brand-blue: #1f63b0;
    --soft-blue: #9bbbd9;
    --field-blue: #b5cde5;
    --icon-blue: #8ab0d6;
    --green: #7cbf4a;
    --line-green: #93c66d;
    --text: #333333;
    --muted: #606060;
    --white: #ffffff;
  }
  * { box-sizing: border-box; margin: 0; padding: 0; }
  html, body { width: 1043px; height: 1200px; overflow: hidden; background: var(--white); }
  body { position: relative; font-family: Arial, Helvetica, sans-serif; color: var(--text); }

  .site-header { position: absolute; top: 0; left: 0; width: 1043px; height: 107px; }
  .brand { position: absolute; left: 26px; top: 40px; display: flex; align-items: center; gap: 10px; }
  .brand-mark { width: 22px; height: 22px; background: var(--brand-blue); }
  .brand-name { font-family: "PT Sans", sans-serif; font-weight: 700; font-size: 26px; letter-spacing: 3px; color: var(--navy); }
  .tagline { position: absolute; left: 363px; top: 40px; font-family: "Michroma", sans-serif; font-size: 21px; color: var(--brand-blue); white-space: nowrap; letter-spacing: -0.5px; }
  .tagline .accent { color: var(--green); }
  .connect { position: absolute; right: 28px; top: 40px; text-align: center; }
  .connect-title { font-family: "PT Sans", sans-serif; font-weight: 700; font-size: 14px; color: var(--icon-blue); margin-bottom: 6px; }
  .social { display: flex; gap: 9px; justify-content: center; }
  .social span { width: 30px; height: 30px; border-radius: 50%; background: var(--icon-blue); display: block; }

  .rule-green { position: absolute; left: 0; width: 1043px; height: 4px; background: var(--line-green); }
  .main-nav { position: absolute; top: 111px; left: 0; width: 1043px; height: 44px; background: var(--navy); }
  .main-nav a { position: absolute; top: 14px; font-family: "Michroma", sans-serif; font-size: 12.5px; color: var(--white); text-decoration: none; letter-spacing: 0.2px; }

  .hero { position: absolute; top: 155px; left: 0; width: 1043px; height: 305px;
    background: linear-gradient(90deg, #dcdad6 0%, #8d8e91 22%, #7e7f83 45%, #9a9b97 64%, #c9d59c 80%, #b9cf83 100%); }
  .hero-shadow { position: absolute; top: 460px; left: 150px; width: 600px; height: 18px;
    background: radial-gradient(ellipse at top, rgba(0,0,0,0.12), rgba(0,0,0,0) 70%); }

  .intro { position: absolute; left: 27px; top: 494px; width: 620px; }
  .section-title { font-family: "Krona One", sans-serif; font-size: 21px; color: var(--navy); letter-spacing: -0.3px; }
  .section-title .grey { color: #666666; }
  .intro p { font-size: 14.6px; line-height: 18px; margin-top: 18px; }
  .intro .section-title + p { margin-top: 15px; }

  .checklist-block { position: absolute; left: 27px; top: 724px; width: 620px; }
  .checklist { list-style: none; margin-top: 20px; margin-left: 16px; }
  .checklist li { position: relative; padding-left: 26px; font-size: 14.6px; line-height: 18px; margin-bottom: 9px; }
  .checklist li svg { position: absolute; left: 0; top: 1px; }

  .call-box { position: absolute; left: 27px; top: 920px; }
  .call-text { font-family: "PT Sans", sans-serif; font-weight: 700; font-size: 18px; color: var(--muted); }
  .phone { display: flex; align-items: center; gap: 6px; margin-top: 10px; }
  .phone-number { font-family: "Oswald", sans-serif; font-weight: 500; font-size: 36px; color: #666666; letter-spacing: -0.5px; }

  .newsletter { position: absolute; left: 688px; top: 499px; width: 330px; height: 203px; background: var(--soft-blue); border-radius: 8px; padding: 20px 27px; }
  .newsletter h2 { font-family: Arial, Helvetica, sans-serif; font-weight: 400; font-size: 24px; color: var(--white); margin-left: 4px; }
  .newsletter p { font-size: 12.5px; line-height: 15px; color: var(--white); margin-top: 8px; }
  .email-field { display: block; width: 265px; height: 35px; margin-top: 12px; border: 1px solid #8fb0d2; border-radius: 10px; background: var(--field-blue); }
  .go-button { display: block; width: 77px; height: 33px; margin-top: 12px; border: 0; border-radius: 5px;
    background: linear-gradient(#5a8ccd, #2f6aae); color: var(--white); font-family: "PT Sans", sans-serif; font-weight: 700; font-size: 13px; }

  .testimonials { position: absolute; left: 690px; top: 724px; width: 320px; }
  .testimonials .section-title { color: #4f86bf; font-size: 20px; }
  .quote { margin-top: 18px; font-size: 12px; line-height: 14px; color: var(--muted); }
  .quote cite { display: block; font-style: normal; font-family: "PT Sans", sans-serif; font-weight: 700; font-size: 13.5px; color: #3e76b4; margin-top: 2px; }

  .footer-band { position: absolute; top: 1085px; left: 0; width: 1043px; height: 15px; background: var(--brand-blue); }
  .footer-nav { position: absolute; top: 1123px; left: 0; width: 1043px; text-align: center; font-size: 13px; color: var(--text); }
  .copyright { position: absolute; top: 1150px; left: 0; width: 1043px; text-align: center; font-size: 11px; color: #555555; }
</style>
</head>
<body>
  <header class="site-header">
    <div class="brand">
      <span class="brand-mark"></span>
      <span class="brand-name">QUORNVALE</span>
    </div>
    <div class="tagline">Reader Outreach <span class="accent">Made Plain</span></div>
    <div class="connect">
      <div class="connect-title">CONNECT WITH DOROTHY</div>
      <div class="social">
        <span role="img" aria-label="Chirpnet"></span>
        <span role="img" aria-label="Friendwall"></span>
        <span role="img" aria-label="Orbix+"></span>
        <span role="img" aria-label="Workloop"></span>
      </div>
    </div>
  </header>

  <div class="rule-green" style="top:106px"></div>
  <nav class="main-nav">
    <a style="left:27px">SERVICES</a>
    <a style="left:184px">ABOUT US</a>
    <a style="left:351px">RESOURCES</a>
    <a style="left:535px">OUR CLIENTS</a>
    <a style="left:725px">BLOG</a>
    <a style="left:857px">CONTACT US</a>
  </nav>

  <div class="hero" role="img" aria-label="Photo of a man in a grey suit holding a closed book against a soft green background"></div>
  <div class="hero-shadow"></div>

  <section class="intro">
    <h1 class="section-title">High Impact <span class="grey">Book Marketing</span> for Authors</h1>
    <p>Quornvale Marketing is book marketing service that that provides authors with an effective, affordable approach to marketing their book.</p>
    <p>We provide marketing coaching and consulting services that accelerate book sales, target your ideal reader and develop a community of fans that will promote your book for you.</p>
    <p>Using high impact, low cost marketing strategies, we will develop a book marketing strategy that achieves your goals and accommodates your budget</p>
  </section>

  <section class="checklist-block">
    <h2 class="section-title">Do you</h2>
    <ul class="checklist">
      <li><svg width="17" height="16" viewBox="0 0 17 16"><circle cx="7" cy="9" r="6.5" fill="#2f2f2f"/><path d="M3.5 8.5l3 3.2L15.5 1.5" fill="none" stroke="#5cb83a" stroke-width="2.6" stroke-linecap="round" stroke-linejoin="round"/></svg>Want to be a best selling author, but need someone to show you the way</li>
      <li><svg width="17" height="16" viewBox="0 0 17 16"><circle cx="7" cy="9" r="6.5" fill="#2f2f2f"/><path d="M3.5 8.5l3 3.2L15.5 1.5" fill="none" stroke="#5cb83a" stroke-width="2.6" stroke-linecap="round" stroke-linejoin="round"/></svg>Wonder what is the secret to achieving high book sales?</li>
      <li><svg width="17" height="16" viewBox="0 0 17 16"><circle cx="7" cy="9" r="6.5" fill="#2f2f2f"/><path d="M3.5 8.5l3 3.2L15.5 1.5" fill="none" stroke="#5cb83a" stroke-width="2.6" stroke-linecap="round" stroke-linejoin="round"/></svg>Worry that you aren’t doing the right things to ensure that your book<br>is a success?</li>
      <li><svg width="17" height="16" viewBox="0 0 17 16"><circle cx="7" cy="9" r="6.5" fill="#2f2f2f"/><path d="M3.5 8.5l3 3.2L15.5 1.5" fill="none" stroke="#5cb83a" stroke-width="2.6" stroke-linecap="round" stroke-linejoin="round"/></svg>Need someone to help keep your spirits up and maintain momentum?</li>
    </ul>
  </section>

  <section class="call-box">
    <p class="call-text">Are you ready for results? Call now for a free consultation</p>
    <div class="phone">
      <svg width="36" height="36" viewBox="0 0 36 36"><circle cx="18" cy="18" r="16" fill="none" stroke="#666" stroke-width="2"/><path d="M12 9c-2 1-3 3-2 6 2 6 6 10 11 12 3 1 5 0 6-2l-4-4-3 2c-3-1-5-4-6-6l2-3z" fill="#666"/></svg>
      <span class="phone-number">214-555-0183</span>
    </div>
  </section>

  <aside class="newsletter">
    <h2>Our Newsletter</h2>
    <p>Sign up for our free newsletter and receive our list of Top Chirpnet Tips for Authors Free!</p>
    <input class="email-field" type="email" aria-label="Email address">
    <button class="go-button" type="button">GO</button>
  </aside>

  <aside class="testimonials">
    <h2 class="section-title">Testimonials</h2>
    <blockquote class="quote" style="margin-top:24px">"I would not be where I am, were it not for Dorothy's marketing advice."<cite>- Marta Lindqvist</cite></blockquote>
    <blockquote class="quote" style="margin-top:24px">"We provide marketing coaching and consulting services that accelerate book sales, targetyour ideal.".<cite>- Grant Holloway</cite></blockquote>
    <blockquote class="quote">"A space/box for a short, 10-15 word testimonials. The testimonials will need to change from page to page"<cite>- Nadia Ferreau</cite></blockquote>
    <blockquote class="quote" style="margin-top:30px">"I would not be where I am, were it not for Dorothy's marketing advice."<cite>- Celine Ortaga</cite></blockquote>
  </aside>

  <div class="rule-green" style="top:1083px"></div>
  <div class="footer-band"></div>
  <nav class="footer-nav">SERVICES · ABOUT US · RESOURCES · OUR CLIENTS · BLOG · CONTACT US</nav>
  <p class="copyright">Copyright © 2005 - 2013 Quornvale Consulting. All rights reserved.</p>
</body>
</html>
```